Velmora and Co Business Card Design

Looking for a business card design. Wanting Smart, Clean and Sharp looking to promote Velmora and Co, our Import Export Business - like Black, White and natural textures. I have uploaded our logo. I like a rounded font but open to other ideas
Being that we have a wide range of products on offer we are looking for a neutral yet eye catching card. We would also like to have Import - Export on the business card to be clear on want our business does.

Target Market(s)

Import export market

Industry/Entity Type

Importer

Contact Information for Business Card

Mr Tobias Kernwell
tobias.kernwell@velmoraandco.com.au
+61 (0) 417 630 284
www.velmoraandco.com.au

Font styles to use
Other font styles liked:
• Unsure of actual font name but something rounded and clean

Colors

Designer to choose colors to be used in the design.

Requirements
Must have
• Instagram icon
• Facebook icon

```html
<!DOCTYPE html>
<html lang="en">
<head>
<meta charset="utf-8">
<title>Velmora and Co – Business Card</title>
<link href="https://fonts.googleapis.com/css2?family=Oswald:wght@500;600&family=Poppins:wght@400;600&family=Roboto:ital,wght@1,700&display=swap" rel="stylesheet">
<style>
  :root {
    --backdrop: #8b6d4c;
    --card-dark: #231f20;
    --card-grey: #878787;
    --card-white: #ffffff;
    --ink: #111111;
    --text-light: #ffffff;
  }
  * { margin: 0; padding: 0; box-sizing: border-box; }
  html, body { width: 900px; height: 1200px; overflow: hidden; }
  body { background: var(--backdrop); position: relative; }

  .card { position: absolute; overflow: hidden; box-shadow: 0 8px 18px rgba(0,0,0,.45); }

  /* Front */
  .card-front { left: 86px; top: 136px; width: 737px; height: 433px; background: var(--card-dark); }
  .front-band { position: absolute; left: 0; top: 0; width: 100%; height: 219px; background: var(--card-grey); }
  .front-notch { position: absolute; left: 237px; top: 66px; width: 267px; height: 160px; background: var(--card-dark); }
  .brand-name {
    position: absolute; left: 274px; top: 166px;
    text-align: left; color: var(--text-light);
    font-family: 'Oswald', sans-serif; font-weight: 600;
    font-size: 54px; line-height: 64px; letter-spacing: 0;
  }
  .tagline {
    position: absolute; left: 0; top: 338px; width: 100%;
    text-align: center; color: var(--text-light);
    font-family: 'Roboto', sans-serif; font-style: italic; font-weight: 700;
    font-size: 29px; letter-spacing: .3px;
  }

  /* Back */
  .card-back { left: 81px; top: 632px; width: 742px; height: 432px; background: var(--card-white); }
  .back-band { position: absolute; left: 0; top: 0; width: 100%; height: 143px; background: var(--card-dark); }
  .person-name {
    position: absolute; left: 46px; top: 40px; color: var(--text-light);
    font-family: 'Oswald', sans-serif; font-weight: 600; font-size: 43px; letter-spacing: .3px;
  }
  .contact-list { position: absolute; left: 43px; top: 207px; list-style: none; }
  .contact-item { display: flex; align-items: center; height: 44px; margin-bottom: 22px; }
  .contact-icon { width: 44px; height: 44px; flex: none; }
  .contact-text {
    margin-left: 18px; color: var(--ink);
    font-family: 'Poppins', sans-serif; font-weight: 400; font-size: 20px;
  }
  .contact-text b { font-weight: 600; }
  .social { position: absolute; top: 340px; display: block; width: 45px; height: 45px; }
  .social-one { left: 582px; }
  .social-two { left: 656px; }
</style>
</head>
<body>

<section class="card card-front">
  <div class="front-band"></div>
  <div class="front-notch"></div>
  <div class="brand-name">VELMORA<br>&amp; CO</div>
  <div class="tagline">IMPORT - EXPORT</div>
</section>

<section class="card card-back">
  <div class="back-band">
    <h1 class="person-name">Mr TOBIAS KERNWELL</h1>
  </div>
  <ul class="contact-list">
    <li class="contact-item">
      <svg class="contact-icon" viewBox="0 0 44 44" aria-hidden="true">
        <rect x="1.5" y="1.5" width="41" height="41" fill="none" stroke="#111" stroke-width="3"/>
        <rect x="6" y="6" width="32" height="32" fill="#111"/>
        <path d="M12 19 q10 -7 20 0 v3 h-5 v-3 h-10 v3 h-5z" fill="#fff"/>
        <rect x="14" y="22" width="16" height="10" rx="1" fill="#fff"/>
        <circle cx="22" cy="27" r="3" fill="#111"/>
      </svg>
      <span class="contact-text">+61 (0) 417 630 284</span>
    </li>
    <li class="contact-item">
      <svg class="contact-icon" viewBox="0 0 44 44" aria-hidden="true">
        <rect x="1.5" y="1.5" width="41" height="41" fill="none" stroke="#111" stroke-width="3"/>
        <rect x="6" y="6" width="32" height="32" fill="#111"/>
        <rect x="10" y="14" width="24" height="16" fill="#fff"/>
        <path d="M10 14 L22 24 L34 14 M10 30 L19 22 M34 30 L25 22" fill="none" stroke="#111" stroke-width="1.5"/>
      </svg>
      <span class="contact-text">TOBIAS.KERNWELL@VELMORA<b>AND</b>CO.COM.AU</span>
    </li>
    <li class="contact-item">
      <svg class="contact-icon" viewBox="0 0 44 44" aria-hidden="true">
        <rect x="1.5" y="1.5" width="41" height="41" fill="none" stroke="#111" stroke-width="3"/>
        <rect x="6" y="6" width="32" height="32" fill="#111"/>
        <g fill="none" stroke="#fff" stroke-width="1.6">
          <circle cx="22" cy="22" r="11"/>
          <ellipse cx="22" cy="22" rx="5" ry="11"/>
          <line x1="11" y1="22" x2="33" y2="22"/>
          <line x1="22" y1="11" x2="22" y2="33"/>
          <line x1="13" y1="16" x2="31" y2="16"/>
          <line x1="13" y1="28" x2="31" y2="28"/>
        </g>
      </svg>
      <span class="contact-text">WWW.VELMORA<b>AND</b>CO.COM.AU</span>
    </li>
  </ul>
  <svg class="social social-one" viewBox="0 0 45 45" role="img" aria-label="Social network profile icon">
    <rect x="1.5" y="1.5" width="42" height="42" fill="none" stroke="#111" stroke-width="3"/>
    <rect x="6" y="6" width="33" height="33" fill="#111"/>
  </svg>
  <svg class="social social-two" viewBox="0 0 45 45" role="img" aria-label="Social network profile icon">
    <rect x="1.5" y="1.5" width="42" height="42" fill="none" stroke="#111" stroke-width="3"/>
    <rect x="6" y="6" width="33" height="33" fill="#111"/>
  </svg>
</section>

</body>
</html>
```